Create new HOME PAGE from existing design

Please read carefully and follow instructions or your design will not be considered. Please ask if you have any questions or need more details.
I have an existing ebay store design that I would like to move off ebay and turn into an ecommerce website. The goal for this project is to take the existing design and create a new website HOME PAGE ONLY. After I have the home page design, I will most likely work with the designer to create the additional website pages for the store, but no additional pages are required for this contest, and no coding is requested as part of this project.
The design files for the existing ebay store design are included below. If you need anything else let me know. The instructions are to use the existing design theme and elements to create a new ecommerce website HOME PAGE. This will not be a straight 1 to 1 conversion, I am looking for a new design based off the existing theme. Graphic elements from the existing ebay store design can be used, or new graphic elements can be created to better fit the theme. This current ebay store design has a high degree of graphic detail, and this same level of detail should exist in the new website home page. The same background should be used and the color scheme should not be changed.
Page should be a maximum width of 1200px, and I would like the design to be responsive.
This website will be a mixed ecommerce site that promotes both products and services. The home page will not be entirely dedicated to ecommerce. A large portion of the top section, below the header, will be reserved for promotion boxes or information. I would like a scrolling bar with the manufacturer logos from the "products we sell" page somewhere near the top half of the page. The bottom half of the home page will be used to display a few items or categories. I am open to ideas so don't be afraid to be creative.
Here is an example:
http://www.sonicvarlo.example/
This is similar to what I'm looking for in that most of the page is dedicated to promotion boxes, with only 1 row of items displayed on the home page. Overall I think the page and promotion boxes are too big and I do not want my site to look like this.

```html
<!DOCTYPE html>
<html lang="en">
<head>
<meta charset="utf-8">
<title>Bravel Signal Supply — Home</title>
<link href="https://fonts.googleapis.com/css2?family=Montserrat:wght@500;700&family=Open+Sans:wght@400;600;700&display=swap" rel="stylesheet">
<style>
:root{
  --navy:#1d3f5e;
  --navy-deep:#15304a;
  --sky:#3b9fe3;
  --mist:#e4e5e8;
  --paper:#ffffff;
  --ink:#2b2f36;
  --muted:#7d848e;
}
*{box-sizing:border-box;margin:0;padding:0}
html,body{width:1200px;height:1200px;overflow:hidden;background:var(--paper)}
body{font-family:"Open Sans",Arial,sans-serif;color:var(--ink)}
.page{width:1200px;height:1200px;display:flex;flex-direction:column}

.notice-bar{height:30px;flex:none;background:var(--mist);display:flex;align-items:center;justify-content:center;font-size:11px;letter-spacing:.3px;color:#555}
.notice-bar a{color:var(--navy);margin-left:4px;text-decoration:underline}

.site-header{height:66px;flex:none;background:var(--navy);display:flex;align-items:center;padding:0 56px}
.brand{display:flex;align-items:center;gap:10px;font-family:"Montserrat",Arial,sans-serif;font-weight:700;font-size:14px;letter-spacing:2.5px;color:#fff;text-transform:uppercase}
.brand-dot{width:12px;height:12px;border-radius:50%;background:#fff}
.main-nav{margin-left:auto;display:flex;gap:62px;font-size:11px;font-weight:600;color:#fff;letter-spacing:.5px}

.hero{position:relative;height:380px;flex:none;overflow:hidden;
  background:
    radial-gradient(ellipse 160px 120px at 250px 200px,#5b6672 0%,rgba(91,102,114,0) 100%),
    radial-gradient(ellipse 260px 200px at 560px 120px,#c8c3b6 0%,rgba(200,195,182,0) 100%),
    radial-gradient(ellipse 300px 160px at 620px 330px,#7a4a3c 0%,rgba(122,74,60,0) 100%),
    linear-gradient(90deg,#1a2029 0%,#262e38 35%,#5d6772 52%,#a9b0b6 75%,#8e99a4 100%)}
.hero-photo{position:absolute;inset:0}
.hero-copy{position:absolute;left:690px;top:150px;color:#fff}
.hero-copy h1{font-size:34px;font-weight:700;line-height:1.05;text-transform:uppercase;letter-spacing:.3px}
.hero-copy p{font-size:14px;text-transform:uppercase;margin-top:6px}
.btn-more{display:inline-flex;align-items:center;margin-top:22px;border:1px solid #fff;border-radius:0 8px 8px 0;height:30px;font-size:10px;text-transform:uppercase}
.btn-more .arrow{width:30px;height:30px;background:#fff;display:flex;align-items:center;justify-content:center}
.btn-more .label{padding:0 24px}

.promo-row{height:180px;flex:none;display:grid;grid-template-columns:1fr 1fr 1fr}
.promo{position:relative}
.promo-a{background:radial-gradient(ellipse 120px 90px at 250px 80px,#e2664a 0%,rgba(226,102,74,0) 100%),linear-gradient(135deg,#f4f4f4 0%,#c7ccd2 100%)}
.promo-b{background:radial-gradient(ellipse 110px 140px at 120px 110px,#2f5aa8 0%,rgba(47,90,168,0) 100%),linear-gradient(160deg,#5c7fbd 0%,#26457a 100%)}
.promo-c{background:radial-gradient(ellipse 160px 90px at 280px 50px,#ffffff 0%,rgba(255,255,255,0) 100%),linear-gradient(160deg,#eef3f8 0%,#bfcfdd 100%)}
.promo-tag{position:absolute;left:0;bottom:0;width:200px;height:96px;background:var(--sky);padding:18px 22px;color:#fff;font-size:12px;font-weight:600;line-height:1.4}
.promo-b .promo-tag{left:auto;right:0;top:0;bottom:auto;background:rgba(200,210,222,.55);color:var(--navy)}
.promo-c .promo-tag{background:var(--navy)}
.promo-actions{display:flex;gap:6px;margin-top:10px}
.promo-actions span{height:16px;display:flex;align-items:center;font-size:8px}
.promo-actions .go{width:16px;background:var(--navy);color:#fff;justify-content:center}
.promo-actions .shop{background:var(--sky);color:#fff;padding:0 12px}
.promo-a .promo-actions .shop{background:#fff;color:var(--sky)}
.promo-c .promo-actions .go{background:var(--sky)}

.brands{height:140px;flex:none;background:var(--navy);color:#fff;text-align:center;padding-top:22px}
.section-title{font-size:13px;font-weight:700;letter-spacing:.6px;text-transform:uppercase}
.brand-strip{display:flex;justify-content:center;align-items:center;gap:56px;margin-top:30px;font-size:20px;font-weight:700;position:relative}
.brand-strip .chev{position:absolute;font-weight:400;font-size:22px;opacity:.7}
.brand-strip .prev{left:240px}.brand-strip .next{right:240px}

.best-sellers{height:220px;flex:none;background:linear-gradient(#e9eaec,#d7d9dc);text-align:center;padding-top:20px;color:var(--navy-deep)}
.product-row{display:flex;justify-content:center;margin-top:20px}
.product{width:190px;border-right:1px solid #c4c7cc;padding:0 20px}
.product:last-child{border-right:none}
.product-image{height:92px;border-radius:6px;background:radial-gradient(ellipse 50px 30px at 50% 50%,#2a4a5e 0%,rgba(42,74,94,0) 100%),linear-gradient(#1c1f24,#2c3138)}
.product-name{font-size:10px;font-weight:600;margin-top:10px;color:#444}
.product-price{font-size:9px;color:var(--muted)}

.service-photo{height:104px;flex:none;background:radial-gradient(ellipse 140px 80px at 600px 52px,#3a3f46 0%,rgba(58,63,70,0) 100%),linear-gradient(90deg,#6f7c88,#aab4bd 50%,#7c8893)}

.service-bar{height:80px;flex:none;background:var(--sky);display:flex;justify-content:center;align-items:center;gap:150px}
.service-bar svg{width:30px;height:30px}
</style>
</head>
<body>
<div class="page">
  <div class="notice-bar">IF YOU DON'T SEE WHAT YOU WANT. <a href="#">CONTACT US!</a></div>

  <header class="site-header">
    <div class="brand"><span class="brand-dot"></span>Bravel Signal Supply</div>
    <nav class="main-nav"><span>HOME</span><span>ABOUT</span><span>SHOP</span><span>CONTACT</span></nav>
  </header>

  <section class="hero">
    <svg class="hero-photo" width="1200" height="380" viewBox="0 0 1200 380" role="img" aria-label="Photo of a wall-mounted touch control panel in a modern kitchen interior">
      <defs>
        <linearGradient id="heroShade" x1="0" y1="0" x2="1" y2="1">
          <stop offset="0" stop-color="#2b4f76" stop-opacity=".72"/>
          <stop offset="1" stop-color="#1d3f5e" stop-opacity=".9"/>
        </linearGradient>
      </defs>
      <polygon points="780,0 1200,0 1200,380 600,380" fill="url(#heroShade)"/>
    </svg>
    <div class="hero-copy">
      <h1>An Innovative<br>Company</h1>
      <p>Offering custom designs</p>
      <div class="btn-more">
        <span class="arrow"><svg width="14" height="10" viewBox="0 0 14 10"><path d="M0 5h12M8 1l4 4-4 4" stroke="#1d3f5e" stroke-width="1.5" fill="none"/></svg></span>
        <span class="label">Know More</span>
      </div>
    </div>
  </section>

  <section class="promo-row">
    <div class="promo promo-a" role="img" aria-label="Product photo of a smart home touch panel in hand">
      <div class="promo-tag">Smart Panels<br>Touch control
        <div class="promo-actions"><span class="go">→</span><span class="shop">Shop Now</span></div>
      </div>
    </div>
    <div class="promo promo-b" role="img" aria-label="Product photo of a compact blue speaker unit">
      <div class="promo-tag">Compact Audio<br>Room speakers
        <div class="promo-actions"><span class="go">→</span><span class="shop">Shop Now</span></div>
      </div>
    </div>
    <div class="promo promo-c" role="img" aria-label="Photo of a bright conference room with audio equipment">
      <div class="promo-tag">Conference Kits<br>Ready to install
        <div class="promo-actions"><span class="go">→</span><span class="shop">Shop Now</span></div>
      </div>
    </div>
  </section>

  <section class="brands">
    <h2 class="section-title">Available Brands</h2>
    <div class="brand-strip">
      <span class="chev prev">‹</span>
      <span>Orvane</span><span>Telmo</span><span>Kestrel</span><span>Lumaro</span><span>Ferrix</span>
      <span class="chev next">›</span>
    </div>
  </section>

  <section class="best-sellers">
    <h2 class="section-title">Our Best Sellers</h2>
    <div class="product-row">
      <div class="product"><div class="product-image" role="img" aria-label="Product photo of a black keypad controller"></div><p class="product-name">Keypad Pro</p><p class="product-price">Retail $249</p></div>
      <div class="product"><div class="product-image" role="img" aria-label="Product photo of a black keypad controller"></div><p class="product-name">Keypad Mini</p><p class="product-price">Retail $189</p></div>
      <div class="product"><div class="product-image" role="img" aria-label="Product photo of a black scene keypad"></div><p class="product-name">Scene Keypad</p><p class="product-price">Retail $219</p></div>
      <div class="product"><div class="product-image" role="img" aria-label="Product photo of a black wall dimmer"></div><p class="product-name">Wall Dimmer</p><p class="product-price">Retail $129</p></div>
    </div>
  </section>

  <div class="service-photo" role="img" aria-label="Photo of a technician installing audio equipment"></div>

  <section class="service-bar">
    <svg viewBox="0 0 30 30" aria-label="Installation"><rect x="4" y="18" width="22" height="8" fill="none" stroke="#1d3f5e" stroke-width="2"/><path d="M9 18v-6h12v6" fill="none" stroke="#1d3f5e" stroke-width="2"/></svg>
    <svg viewBox="0 0 30 30" aria-label="Support"><circle cx="15" cy="8" r="4" fill="none" stroke="#1d3f5e" stroke-width="2"/><path d="M7 27c0-6 4-10 8-10s8 4 8 10" fill="none" stroke="#1d3f5e" stroke-width="2"/></svg>
    <svg viewBox="0 0 30 30" aria-label="Pricing"><text x="15" y="24" text-anchor="middle" font-family="Open Sans, sans-serif" font-size="24" fill="#1d3f5e">$</text></svg>
    <svg viewBox="0 0 30 30" aria-label="Service"><path d="M6 24l11-11M17 13a5 5 0 1 0 4-8l-3 3 2 2 3-3a5 5 0 0 1-6 6" fill="none" stroke="#1d3f5e" stroke-width="2"/></svg>
  </section>
</div>
</body>
</html>
```